Civil engineering company | Billboard

We need a billboard design for Velmora- civil engineering company. We want big logo in the center of billboard and web site (www.velmora.hr) below the logo. Also, we want an subtle abstract pattern in the background. Dimensions of the billboard are: width :10 m, height: 2m. Design must be celan and modern.
Industry/Entity Type
Civil engineering
Font styles to use
Sans Serif
Colors
F0912C
F2A743
F7CA91
FBE8D2
FDF5EE
Requirements
Must have
- Logo and new unique pattern design for Velomra company
Should not have
- pictures of construction machinery and tools

```html
<!DOCTYPE html>
<html lang="hr">
<head>
<meta charset="utf-8">
<title>Velmora billboard</title>
<link rel="stylesheet" href="https://fonts.googleapis.com/css2?family=Michroma&family=Quicksand:wght@500&display=swap">
<style>
  :root {
    --orange: #e8913a;
    --orange-light: #f2a743;
    --orange-pale: #f7ca91;
    --grey: #5b5b5b;
    --grey-light: #8a8a8a;
    --text-dark: #3a3a3a;
    --panel: #ffffff;
    --backdrop: #eef1f4;
  }
  html, body {
    margin: 0;
    padding: 0;
    overflow: hidden;
  }
  .canvas {
    position: relative;
    width: 1200px;
    height: 952px;
    background: var(--backdrop);
    overflow: hidden;
  }
  .billboard {
    position: absolute;
    left: 142px;
    top: 362px;
    width: 1012px;
    height: 202px;
    background: var(--panel);
    box-shadow: 0 2px 10px rgba(0,0,0,0.12);
    overflow: hidden;
  }
  .brand-mark {
    position: absolute;
    left: 62px;
    top: 48px;
    width: 104px;
    height: 104px;
    border: 2px solid var(--grey);
  }
  .brand-name {
    position: absolute;
    left: 182px;
    top: 39px;
    margin: 0;
    font-family: "Michroma", sans-serif;
    font-weight: 400;
    font-size: 72px;
    line-height: 1;
    color: var(--orange);
    letter-spacing: 0.01em;
    white-space: nowrap;
  }
  .brand-url {
    position: absolute;
    left: 230px;
    top: 115px;
    margin: 0;
    font-family: "Quicksand", sans-serif;
    font-weight: 500;
    font-size: 34px;
    line-height: 1;
    letter-spacing: 0.18em;
    color: var(--text-dark);
    white-space: nowrap;
  }
  .pattern-area {
    position: absolute;
    right: 0;
    top: 0;
    width: 340px;
    height: 202px;
    background: linear-gradient(135deg, var(--orange-pale) 0%, var(--orange-light) 35%, var(--orange) 60%, var(--grey-light) 85%, var(--grey) 100%);
    clip-path: polygon(58% 0, 100% 0, 100% 100%, 0 100%);
  }
</style>
</head>
<body>
  <main class="canvas">
    <section class="billboard">
      <div class="brand-mark" aria-hidden="true"></div>
      <h1 class="brand-name">VELMORA</h1>
      <p class="brand-url">www.velmora.hr</p>
      <div class="pattern-area" role="img" aria-label="Abstract background pattern of nested orange and grey chevrons rising diagonally in the right corner"></div>
    </section>
  </main>
</body>
</html>
```